Varnel Psychiatry (Psychiatry clinic offering cutting edge treatments)

2 sided flyer for new psychiatry practice in Boulder, CO. I want something that looks professional, cutting edge, but also welcoming and friendly. My logo and pictures are attached.

Some of the copy:
Personalized, holistic Psychiatry combined with cutting-edge, evidence-based treatments. Our personalized psychiatry plan includes a bio-psycho-social evaluation, personalized treatment plan, medical evaluation for underlying hormonal and electrolyte abnormalities, and genetic testing (when warranted).

We specialize in treatment-resistant depression and substance abuse. We also treat PTSD, Bipolar Disorder, OCD, anxiety disorders, ADHD, and psychotic disorders.

About Dr. Brok- Dr. Brok served as Chief Resident at the largest private psychiatry hospital in Colorado. While there he won 3 consecutive awards for exceptionally high Psychiatry in service test score (99th percentile). He was a board member of Kestrel Mind Guild and helped advocate for better Colorado mental health policy. Dr. Brok is uniquely trained in Ketamine, Transcranial Magnetic Stimulation, and integrative psychiatry.

Target Market(s)

Private pay mental health patients, planning to give out to psychologists and family practice doctors

Industry/Entity Type

Medicine/Psychiatry

Colors
0054AA
0677BA
7BADD7
CADEEF
E8F1F8
0094D4
00A9DD
6FCCEA
C7EBF8
E9F6FB
00AB8E
00BBA5
67D7C9
C6EFE9
E9F9F6

Requirements
Must have
• My logo, an about me (Dr. Tomas Brok) section

```html
<!DOCTYPE html>
<html lang="en">
<head>
<meta charset="utf-8">
<title>Varnel Psychiatry – Two-Sided Flyer</title>
<link href="https://fonts.googleapis.com/css2?family=Oswald:wght@500&family=Source+Sans+3:wght@400;600;700&display=swap" rel="stylesheet">
<style>
  :root{
    --stage:#84858a;
    --paper:#ffffff;
    --navy:#24306b;
    --footer:#22285a;
    --ink:#2b3470;
    --teal:#62c9e2;
    --blue:#3d80c6;
    --purple:#8b57b1;
    --lavender:#eeedf7;
    --logo-grey:#4d5261;
    --link:#3a8fc4;
  }
  *{box-sizing:border-box;margin:0;padding:0}
  html,body{width:1200px;height:775px;overflow:hidden}
  body{background:var(--stage);font-family:"Source Sans 3",sans-serif;color:var(--ink);position:relative}
  .flyer{position:absolute;top:70px;width:495px;height:641px;background:var(--paper);overflow:hidden;box-shadow:2px 3px 6px rgba(0,0,0,.35)}
  .flyer--front{left:95px}
  .flyer--back{left:643px;width:494px}

  .brand{position:absolute;left:24px;top:22px;display:flex;align-items:center;gap:8px}
  .brand__dot{width:34px;height:34px;border-radius:50%;background:linear-gradient(135deg,var(--teal),var(--purple))}
  .brand__name{font-size:20px;font-weight:600;color:var(--logo-grey);letter-spacing:.5px;text-transform:uppercase}

  .announce{position:absolute;right:26px;top:28px;text-align:right;font-family:"Oswald",sans-serif;font-weight:500;font-size:12.5px;line-height:14px;color:var(--navy);text-transform:uppercase;transform:scaleX(.88);transform-origin:right}
  .announce span{color:var(--link)}

  .hero{position:absolute;left:18px;top:67px;width:466px;height:227px;border-top-right-radius:34px}
  .flyer--front .hero{background:linear-gradient(100deg,#e9eef5 0%,#c9d3e3 35%,#6b6c9e 60%,#8a4f8e 85%,#5b7fb8 100%)}
  .flyer--back .hero{background:linear-gradient(100deg,#dfe3e6 0%,#b9bec3 30%,#8f8a86 55%,#c7c4c0 80%,#e8e8e6 100%)}
  .hero__tag{position:absolute;left:17px;top:94px;font-size:13px;line-height:17px;font-weight:700;color:var(--ink);text-transform:uppercase}

  .intro{position:absolute;left:18px;top:305px;width:459px;font-size:9px;line-height:12.5px;text-align:justify;color:#1f2a60}

  .conditions{position:absolute;left:0;top:350px;width:495px;height:65px;display:flex;background:linear-gradient(90deg,#62c9e2,#3d80c6 50%,#8b57b1)}
  .condition{flex:1;border-right:1.5px solid rgba(255,255,255,.7);display:flex;flex-direction:column;align-items:center;justify-content:flex-end;padding-bottom:7px;color:#fff;font-size:9.5px;line-height:10px;text-align:center}
  .condition:last-child{border-right:none}
  .condition svg{margin-bottom:auto;margin-top:7px}

  .textured{position:absolute;left:0;width:100%;background:var(--lavender)}
  .flyer--front .textured{top:415px;height:200px}
  .flyer--back .textured{top:444px;height:170px}

  .body-copy{position:absolute;left:18px;top:502px;width:459px;font-size:7.3px;line-height:10.5px;text-align:justify;color:var(--ink)}
  .body-copy p{margin-bottom:8px}

  .focus{position:absolute;left:0;top:315px;width:494px;height:129px;background:linear-gradient(90deg,#6fcfe4,#3f8fcb 45%,#8b57b1);color:#fff;padding:12px 17px 0}
  .focus h2{font-size:12.5px;line-height:17px;font-weight:700;text-align:center;text-transform:uppercase;margin-bottom:8px}
  .focus p{font-size:8.3px;line-height:11.7px;text-align:justify}

  .doctor{position:absolute;left:16px;top:462px;width:353px}
  .doctor h3{font-size:12.5px;font-weight:700;color:var(--ink);text-transform:uppercase;margin-bottom:3px}
  .doctor p{font-size:6.9px;line-height:10.4px;text-align:justify;color:var(--ink)}
  .portrait{position:absolute;left:380px;top:478px;width:101px;height:98px;background:linear-gradient(160deg,#d8d8d8,#8a8a8a 55%,#3e3e3e)}
  .cta{position:absolute;left:14px;top:580px;font-size:10.5px;color:var(--link)}

  .contact{position:absolute;left:0;bottom:0;width:100%;height:39px;background:var(--footer);border-top-left-radius:22px;border-top-right-radius:22px;display:flex;align-items:center;justify-content:space-between;padding:0 20px 0 15px;color:#fff;font-size:10px}
  .contact__item{display:flex;align-items:center;gap:5px}
</style>
</head>
<body>

<section class="flyer flyer--front">
  <div class="brand"><div class="brand__dot"></div><div class="brand__name">Varnel Psychiatry</div></div>
  <div class="announce">Varnel Psychiatry is now accepting<br>new patients in <span>Boulder, Colorado!</span></div>

  <div class="hero" role="img" aria-label="Photo of a woman in profile with a glowing digital neural network">
    <p class="hero__tag">Specializing in<br>evidence-based,<br>state-of-the-art<br>mental health<br>treatment.</p>
  </div>

  <p class="intro">We specialize in treating patients with treatment resistant depression and substance abuse disorders who have not responded to other forms of treatment. We believe that by providing comprehensive care, we can help our patients heal both emotionally and physically. We also treat patients with:</p>

  <div class="conditions">
    <div class="condition"><svg width="30" height="30" viewBox="0 0 30 30" fill="none" stroke="#fff" stroke-width="1.2"><ellipse cx="15" cy="14" rx="11" ry="9"/><path d="M15 5v18M9 10h3M18 10h3M8 16h4M18 16h4"/><circle cx="12" cy="10" r="1"/><circle cx="18" cy="16" r="1"/></svg>PTSD</div>
    <div class="condition"><svg width="30" height="30" viewBox="0 0 30 30" fill="none" stroke="#fff" stroke-width="1.2"><circle cx="15" cy="13" r="9"/><path d="M11 22v5M19 22v5"/><circle cx="12.5" cy="12" r="2.5"/><circle cx="17.5" cy="12" r="2.5"/></svg>Bipolar<br>Disorder</div>
    <div class="condition"><svg width="30" height="30" viewBox="0 0 30 30" fill="none" stroke="#fff" stroke-width="1.2"><circle cx="13" cy="12" r="9"/><path d="M19.5 18.5l7 7"/><path d="M10.5 10a2.5 2.5 0 1 1 3.5 2.3v1.7"/><circle cx="14" cy="16.5" r=".6" fill="#fff"/></svg>OCD</div>
    <div class="condition"><svg width="30" height="30" viewBox="0 0 30 30" fill="none" stroke="#fff" stroke-width="1.2"><circle cx="15" cy="14" r="10"/><path d="M10 14c2-3 4 3 6 0s3 3 4 0"/><path d="M12 26h6"/></svg>Anxiety<br>Disorders</div>
    <div class="condition"><svg width="30" height="30" viewBox="0 0 30 30" fill="none" stroke="#fff" stroke-width="1.2"><circle cx="15" cy="13" r="8"/><path d="M11 21v6M19 21v6"/><path d="M15 9l-2 4h4l-2 4"/></svg>ADHD</div>
    <div class="condition"><svg width="30" height="30" viewBox="0 0 30 30" fill="none" stroke="#fff" stroke-width="1.2"><circle cx="15" cy="13" r="10"/><path d="M10 13c0-4 10-4 10 0s-6 3-5 0"/><path d="M12 23v4M18 23v4"/></svg>Psychotic<br>Disorders</div>
  </div>

  <div class="textured" role="img" aria-label="Light lavender dotted texture"></div>

  <div class="body-copy" style="top:435px">
    <p>We know that mental health is complex and that multiple factors can contribute to the development of mental illness. For this reason, we take an integrative approach that considers the whole person. We understand that each individual has their own unique set of experiences, strengths, and challenges, and we tailor our treatment plans to suit each patient's personal needs.</p>
    <p>We know that mental health is complex and that multiple factors can contribute to the development of mental illness. For this reason, we take an integrative approach that considers the whole person. We understand that each individual has their own unique set of experiences, strengths, and challenges, and we tailor our treatment plans to suit each patient's personal needs. So often, when we think about mental health, we focus on just treating symptoms. If someone is depressed, they might take medication to help them feel better. If someone is anxious, they might see a therapist to help them manage their anxiety.</p>
    <p>While these treatments can be helpful, they only address the symptoms of mental illness. To truly address mental health, it is necessary to treat the root causes. This might involve addressing childhood trauma, unresolved conflict, or feelings of worthlessness. It might also involve developing healthy coping mechanisms and learning how to set boundaries. By treating the root causes of mental illness, we can begin to create lasting change suited to each patient's personal needs.</p>
  </div>

  <footer class="contact">
    <span class="contact__item"><svg width="10" height="10" viewBox="0 0 10 10" fill="none" stroke="#fff" stroke-width="1"><circle cx="5" cy="5" r="4.3"/><path d="M5 2.3a1.8 1.8 0 0 0-1.8 1.8C3.2 5.5 5 7.6 5 7.6s1.8-2.1 1.8-3.5A1.8 1.8 0 0 0 5 2.3z"/></svg>1840 Alder Ave. Boulder, CO 80302 #110</span>
    <span class="contact__item"><svg width="10" height="10" viewBox="0 0 10 10" fill="none" stroke="#fff" stroke-width="1"><circle cx="5" cy="5" r="4.3"/><path d="M3.2 2.8l1 1-.6.7a3.5 3.5 0 0 0 1.9 1.9l.7-.6 1 1-.7.7c-2 0-4-2-4-4z"/></svg>303-555-0148</span>
    <span class="contact__item"><svg width="10" height="10" viewBox="0 0 10 10" fill="none" stroke="#fff" stroke-width="1"><circle cx="5" cy="5" r="4.3"/><circle cx="5" cy="5" r="2"/></svg>www.varnelpsych.com</span>
  </footer>
</section>

<section class="flyer flyer--back">
  <div class="brand"><div class="brand__dot"></div><div class="brand__name">Varnel Psychiatry</div></div>
  <div class="announce">Varnel Psychiatry is now accepting<br>new patients in <span>Boulder, Colorado!</span></div>

  <div class="hero" role="img" aria-label="Photo of a psychiatrist consulting with a couple at a desk with a laptop"></div>

  <div class="focus">
    <h2>Specializing in evidence-based, state-of-the-art<br>mental health treatment.</h2>
    <p>Our personalized psychiatry plan includes a bio-psycho-social evaluation, tailored treatment plan, medical evaluation for underlying hormonal and electrolyte abnormalities, and genetic testing (when warranted). Our integrative psychiatry approach combines cutting edge, evidence-based treatments with holistic therapies to provide you with the best possible care. In addition, we also offer Ketamine Assisted Therapy, TMS (Transcranial Magnetic Simulation), and MAT Treatment for Substance abuse. We pride ourselves on always staying up to date on the latest mental health treatments.</p>
  </div>

  <div class="textured" role="img" aria-label="Light lavender dotted texture"></div>

  <div class="doctor">
    <h3>Dr. Tomas Brok</h3>
    <p>Dr. Tomas Brok is a psychiatrist with years of experience providing compassionate, evidence-based care to patients of all ages. He is uniquely trained in several cutting-edge treatments, including Ketamine, Transcranial Magnetic Stimulation (TMS), and integrative psychiatry. Prior to founding Varnel Psychiatry, Dr. Brok served as Chief Resident at the largest private psychiatry hospital in Colorado. While there, he won three consecutive awards for exceptionally high Psychiatry in-service test scores (99th percentile). In addition, he was a board member of the Kestrel Mind Guild and helped advocate for better Colorado mental health policy. Thanks to his extensive training and experience, Dr. Brok is able to provide each patient with an individualized treatment plan that brings optimum results.</p>
  </div>
  <div class="portrait" role="img" aria-label="Black and white portrait photo of Dr. Tomas Brok"></div>
  <p class="cta">Get started with Varnel, today!</p>

  <footer class="contact">
    <span class="contact__item"><svg width="10" height="10" viewBox="0 0 10 10" fill="none" stroke="#fff" stroke-width="1"><circle cx="5" cy="5" r="4.3"/><path d="M5 2.3a1.8 1.8 0 0 0-1.8 1.8C3.2 5.5 5 7.6 5 7.6s1.8-2.1 1.8-3.5A1.8 1.8 0 0 0 5 2.3z"/></svg>1840 Alder Ave. Boulder, CO 80302 #110</span>
    <span class="contact__item"><svg width="10" height="10" viewBox="0 0 10 10" fill="none" stroke="#fff" stroke-width="1"><circle cx="5" cy="5" r="4.3"/><path d="M3.2 2.8l1 1-.6.7a3.5 3.5 0 0 0 1.9 1.9l.7-.6 1 1-.7.7c-2 0-4-2-4-4z"/></svg>303-555-0148</span>
    <span class="contact__item"><svg width="10" height="10" viewBox="0 0 10 10" fill="none" stroke="#fff" stroke-width="1"><circle cx="5" cy="5" r="4.3"/><circle cx="5" cy="5" r="2"/></svg>www.varnelpsych.com</span>
  </footer>
</section>

</body>
</html>
```